Brochure Design: Text Messaging Service

We are looking for a brochure design for our new text messaging service. this should be a 2 page design on a 8.5x11" page
this should a clean design that catshed the eyey and features the features and benefits.
the brochure should bew designed so that we can entice our existing business clients to adopt this new service for their business.

Target Market(s)

business owner

Industry/Entity Type

Driving School

Font styles to use
Sans Serif

Colors
0692cd
33b8a4

Requirements
Must have
• pricing info, features, and screen shot on a computer. maybe also include image of your teen with cell phone.
Nice to have
• n/a
Should not have
• n/a

```html
<!DOCTYPE html>
<html lang="en">
<head>
<meta charset="utf-8">
<title>Text Messaging Brochure</title>
<link href="https://fonts.googleapis.com/css2?family=Exo+2:wght@600;700&family=PT+Sans:wght@400;700&family=Oswald:wght@500&display=swap" rel="stylesheet">
<style>
  :root {
    --brand-blue: #0692cd;
    --brand-teal: #33b8a4;
    --ink: #555b61;
    --ink-soft: #6b7178;
    --paper: #ffffff;
    --paper-tint: #f3f4f5;
    --backdrop: #e6e7e8;
  }
  * { box-sizing: border-box; margin: 0; padding: 0; }
  html, body { width: 1200px; height: 803px; overflow: hidden; }
  body {
    background: var(--backdrop);
    font-family: "PT Sans", Arial, sans-serif;
    color: var(--ink);
    position: relative;
  }
  .page {
    position: absolute;
    top: 41px;
    width: 556px;
    height: 720px;
    background: var(--paper);
    box-shadow: 0 2px 10px rgba(0,0,0,.12);
    overflow: hidden;
  }
  .page--front { left: 29px; }
  .page--back { left: 615px; background: var(--paper-tint); }

  .masthead {
    height: 101px;
    background: var(--paper);
    position: relative;
  }
  .brand {
    position: absolute;
    left: 18px;
    top: 36px;
    display: flex;
    align-items: center;
    gap: 8px;
  }
  .brand__dot {
    width: 22px; height: 22px; border-radius: 50%;
    background: var(--brand-teal);
  }
  .brand__name {
    font-family: "Exo 2", Arial, sans-serif;
    font-weight: 700;
    font-size: 20px;
    color: var(--brand-blue);
  }
  .masthead__title {
    position: absolute;
    right: 28px;
    top: 32px;
    text-align: right;
  }
  .masthead__title h1 {
    font-family: "Exo 2", Arial, sans-serif;
    font-weight: 700;
    font-size: 25px;
    color: var(--brand-blue);
    line-height: 1;
  }
  .masthead__title p {
    font-family: "Exo 2", Arial, sans-serif;
    font-weight: 600;
    font-size: 13.5px;
    letter-spacing: .6px;
    color: var(--ink);
    margin-top: 6px;
  }

  .photo { position: absolute; left: 0; width: 100%; }
  .photo--student {
    top: 101px; height: 286px;
    background: linear-gradient(100deg, #c8a58b 0%, #e9d8c6 35%, #dfe2e6 65%, #c9cfd6 100%);
  }
  .photo--laptop {
    top: 101px; height: 304px;
    background: linear-gradient(160deg, #d9dee3 0%, #f1f2f3 45%, #c7c9cb 75%, #d7c3a6 100%);
  }

  .band {
    position: absolute; left: 0; width: 100%;
    background: var(--brand-teal);
    color: #fff;
  }
  .band--front {
    top: 387px; height: 77px;
    padding: 7px 206px 0 19px;
    font-size: 10.3px;
    line-height: 1.27;
    text-align: justify;
  }
  .band--back {
    top: 405px; height: 72px;
    padding: 20px 26px 0 27px;
    font-size: 11.6px;
    line-height: 1.5;
  }

  .phone-shot {
    position: absolute;
    left: 382px; top: 361px;
    width: 174px; height: 313px;
    background: linear-gradient(180deg, #2f3a44 0%, #3c4853 55%, #c9a487 85%, #b98f72 100%);
    border-radius: 20px 0 0 0;
  }

  .body-copy {
    position: absolute;
    left: 19px; top: 472px;
    width: 288px;
    font-size: 9.4px;
    line-height: 1.2;
    color: var(--ink-soft);
    text-align: justify;
  }
  .body-copy p + p { margin-top: 10px; }

  .cta {
    position: absolute; left: 0; bottom: 0;
    width: 100%; height: 46px;
    background: var(--brand-blue);
    color: #fff;
    font-size: 17px;
    text-align: center;
    line-height: 46px;
  }

  .price-badge {
    position: absolute;
    left: 27px; top: 147px;
    width: 128px; height: 128px;
    border-radius: 50%;
    background: var(--brand-blue);
    border: 6px solid #fff;
    box-shadow: 0 2px 6px rgba(0,0,0,.2);
    color: #fff;
    font-family: "Oswald", Arial, sans-serif;
    font-weight: 500;
    text-align: center;
  }
  .price-badge__lead { font-size: 12px; margin-top: 22px; letter-spacing: .3px; }
  .price-badge__amount { font-size: 38px; line-height: 1; margin-top: 2px; }
  .price-badge__amount small { font-size: 11px; vertical-align: middle; margin-right: 2px; }
  .price-badge__unit { font-size: 12px; margin-top: 2px; }

  .features__tab {
    position: absolute;
    left: 0; top: 500px;
    width: 172px; height: 28px;
    background: var(--brand-blue);
    border-radius: 0 14px 14px 0;
    color: #fff;
    font-size: 20px;
    line-height: 28px;
    padding-left: 40px;
  }
  .features__list {
    position: absolute;
    top: 542px;
    list-style: none;
    font-size: 13.5px;
    color: var(--ink);
  }
  .features__list--left { left: 27px; }
  .features__list--right { left: 292px; width: 230px; }
  .features__list li {
    display: flex;
    align-items: flex-start;
    gap: 6px;
    line-height: 19.5px;
  }
  .features__list svg { flex: none; margin-top: 5px; }
  .features__note {
    position: absolute;
    left: 307px; top: 648px;
    font-size: 8.8px;
    color: var(--ink);
  }
</style>
</head>
<body>

<section class="page page--front">
  <header class="masthead">
    <div class="brand"><span class="brand__dot"></span><span class="brand__name">RoadReady Software</span></div>
    <div class="masthead__title">
      <h1>Text Messaging</h1>
      <p>www.roadreadysoftware.com</p>
    </div>
  </header>

  <div class="photo photo--student" role="img" aria-label="Photo of a smiling teenage student texting on her phone in a school hallway"></div>

  <div class="band band--front">
    SMS Communication Module (Short Message Service; “Text Message”) is designed to allow your school to effectively communicate with both parents and students in real-time. In today’s world, both students and parents expect almost instant communication with their friends, family, and driving school.
  </div>

  <div class="phone-shot" role="img" aria-label="Photo of a hand holding a smartphone showing the SMS dashboard"></div>

  <div class="body-copy">
    <p>With our Integrated Text Messaging Module, your driving school can automatically send reminders for upcoming classroom sessions, in-car lessons, road tests, urgent notifications and more! Not only will students and parents receive these reminders, but they will have the ability to respond and you will see their response on your admin portal.</p>
    <p>Each driving school will have their choice of using a local phone number or a toll-free number, which will be dedicated to your school. We have fully integrated this module with our software to eliminate the need to go through a third-party service. This will save time and money for you and your staff.</p>
    <p>In order to receive these SMS messages, each customer will be have the option to opt into SMS notifications at the time of enrollment. This decision is not set in stone and at any point they can add or remove phone numbers at which they want to stop or start receiving notifications.</p>
  </div>

  <footer class="cta">Please call 888.555.0147 to signup or learn more.</footer>
</section>

<section class="page page--back">
  <header class="masthead">
    <div class="brand"><span class="brand__dot"></span><span class="brand__name">RoadReady Software</span></div>
    <div class="masthead__title">
      <h1>Text Messaging</h1>
      <p>www.roadreadysoftware.com</p>
    </div>
  </header>

  <div class="photo photo--laptop" role="img" aria-label="Photo of a laptop on a desk showing the SMS message screen, with a latte beside it"></div>

  <div class="price-badge">
    <div class="price-badge__lead">PLANS STARTING</div>
    <div class="price-badge__amount"><small>AT</small>$25</div>
    <div class="price-badge__unit">MONTH</div>
  </div>

  <div class="band band--back">
    Our Text Messaging Module is one of many very exciting upcoming features and functionalities that will be rolled out to clients in the near future! Signup today with plans starting as little as $25/month!
  </div>

  <div class="features__tab">FEATURES</div>

  <ul class="features__list features__list--left">
    <li><svg width="9" height="9" viewBox="0 0 10 10"><circle cx="5" cy="5" r="5" fill="#0692cd"/><path d="M4 2.8 6.2 5 4 7.2" stroke="#fff" stroke-width="1.4" fill="none"/></svg>Dedicated local or toll-free number</li>
    <li><svg width="9" height="9" viewBox="0 0 10 10"><circle cx="5" cy="5" r="5" fill="#0692cd"/><path d="M4 2.8 6.2 5 4 7.2" stroke="#fff" stroke-width="1.4" fill="none"/></svg>Custom message content</li>
    <li><svg width="9" height="9" viewBox="0 0 10 10"><circle cx="5" cy="5" r="5" fill="#0692cd"/><path d="M4 2.8 6.2 5 4 7.2" stroke="#fff" stroke-width="1.4" fill="none"/></svg>Delivery confirmation</li>
    <li><svg width="9" height="9" viewBox="0 0 10 10"><circle cx="5" cy="5" r="5" fill="#0692cd"/><path d="M4 2.8 6.2 5 4 7.2" stroke="#fff" stroke-width="1.4" fill="none"/></svg>Two-way messaging</li>
    <li><svg width="9" height="9" viewBox="0 0 10 10"><circle cx="5" cy="5" r="5" fill="#0692cd"/><path d="M4 2.8 6.2 5 4 7.2" stroke="#fff" stroke-width="1.4" fill="none"/></svg>Automatic messaging</li>
  </ul>

  <ul class="features__list features__list--right">
    <li><svg width="9" height="9" viewBox="0 0 10 10"><circle cx="5" cy="5" r="5" fill="#0692cd"/><path d="M4 2.8 6.2 5 4 7.2" stroke="#fff" stroke-width="1.4" fill="none"/></svg>Phone number validation</li>
    <li><svg width="9" height="9" viewBox="0 0 10 10"><circle cx="5" cy="5" r="5" fill="#0692cd"/><path d="M4 2.8 6.2 5 4 7.2" stroke="#fff" stroke-width="1.4" fill="none"/></svg>Online enrollment integration</li>
    <li><svg width="9" height="9" viewBox="0 0 10 10"><circle cx="5" cy="5" r="5" fill="#0692cd"/><path d="M4 2.8 6.2 5 4 7.2" stroke="#fff" stroke-width="1.4" fill="none"/></svg>Bulk messaging</li>
    <li><svg width="9" height="9" viewBox="0 0 10 10"><circle cx="5" cy="5" r="5" fill="#0692cd"/><path d="M4 2.8 6.2 5 4 7.2" stroke="#fff" stroke-width="1.4" fill="none"/></svg><span>Plans starting at $25/month (includes 500 messages)*</span></li>
  </ul>

  <p class="features__note">*Additional messages $.03/message</p>

  <footer class="cta">Please call 888.555.0147 to signup or learn more.</footer>
</section>

</body>
</html>
```